Business card and (possibly) logo

Hi - we need a new business card.
We have an existing logo that we quite like but we are open to options.
We are an architectural firm - we specialize in upmarket residential work and apartment blocks.
We are chasing a business card at present but also want to extensively update our website going forward to attract a much higher level of client / investor / developer.
Our current logo is black, grey and yellow and based on the sun/moon temples in Mexico.
We are open to variations.
We want to communicate professionalism, trust, quality.
Our website is www.korvalstudio.com.au - but note as above - we want to change the website as well to be a lot 'classier' and to appeal to a higher end market.

thanks

Target Market(s)

We are an architect firm - our target market is Developers and builders of high end houses and luxury apartment blocks. Also private home owners wanting to build excellent expensive houses. (ideally over $1m budgets)

Industry/Entity Type

Residential

Requirements
Must have
• Logo
Contact details;
Name
phone, mobile, email, web

```html
<!DOCTYPE html>
<html lang="en">
<head>
<meta charset="utf-8">
<title>Korval Studio – Business Card</title>
<link rel="stylesheet" href="https://fonts.googleapis.com/css2?family=Cinzel:wght@400;700&family=Kaushan+Script&family=Lora:wght@400;700&display=swap">
<style>
  :root {
    --page: #ffffff;
    --card-dark: #0b0b0b;
    --card-dark-mid: #2a2a2a;
    --gold: #c9a43a;
    --gold-line: #8a7535;
    --brand-yellow: #f2d31b;
    --ink: #2b2b2b;
    --ink-soft: #555555;
    --card-light: #ffffff;
    --card-border: #8a8a8a;
    --watermark: rgba(0,0,0,0.07);
  }
  * { margin: 0; padding: 0; box-sizing: border-box; }
  html, body { width: 1200px; height: 900px; overflow: hidden; background: var(--page); }
  .canvas { position: relative; width: 1200px; height: 900px; }

  /* Front side */
  .card-front {
    position: absolute; left: 312px; top: 104px; width: 576px; height: 334px;
    background: var(--card-dark); overflow: hidden;
  }
  .card-front__texture {
    position: absolute; inset: 0;
    background: radial-gradient(ellipse at 50% 45%, var(--card-dark-mid) 0%, #151515 45%, var(--card-dark) 80%);
  }
  .card-front__frame {
    position: absolute; left: 13px; top: 14px; width: 550px; height: 307px;
    border: 1.5px solid var(--gold-line);
  }
  .brand-mark {
    position: absolute; left: 0; right: 0; top: 120px; text-align: center;
    font-family: "Cinzel", serif; font-weight: 700; color: var(--brand-yellow);
    line-height: 1;
  }
  .brand-mark__line { display: block; font-size: 40px; letter-spacing: 2px; }
  .brand-mark__line--sub { font-size: 22px; letter-spacing: 4px; margin-top: 6px; }

  /* Back side */
  .card-back {
    position: absolute; left: 312px; top: 464px; width: 574px; height: 326px;
    background: var(--card-light); border: 1px solid var(--card-border); overflow: hidden;
  }
  .card-back__texture {
    position: absolute; inset: 0;
    background: linear-gradient(135deg, #f7f7f7 0%, #ffffff 50%, #f4f4f4 100%);
  }
  .corner-brand {
    position: absolute; left: 9px; top: 36px;
    font-family: "Cinzel", serif; font-weight: 700; font-size: 10px; line-height: 1.05;
    color: rgba(0,0,0,0.16);
  }
  .faint-brand {
    position: absolute; left: 325px; top: 180px; width: 240px; text-align: center;
    font-family: "Cinzel", serif; font-weight: 700; color: var(--watermark); line-height: 1;
  }
  .faint-brand span { display: block; font-size: 44px; }
  .faint-brand span + span { font-size: 26px; margin-top: 4px; letter-spacing: 3px; }

  .address {
    position: absolute; left: 0; width: 600px; top: 19px; text-align: center;
    font-family: "Cinzel", serif; font-size: 11px; color: var(--ink-soft); letter-spacing: 0.5px;
  }
  .divider {
    position: absolute; left: 304px; top: 50px; width: 3px; height: 228px; background: var(--gold);
  }
  .person { position: absolute; right: 283px; top: 136px; text-align: right; }
  .person__name {
    font-family: "Kaushan Script", cursive; font-size: 40px; color: var(--gold); line-height: 1; white-space: nowrap;
  }
  .person__role {
    font-family: "Cinzel", serif; font-size: 13px; color: var(--ink); margin-top: -4px;
  }
  .contacts { position: absolute; left: 322px; top: 118px; list-style: none; }
  .contacts li {
    display: flex; align-items: center; height: 40px;
    font-family: "Lora", serif; font-weight: 700; font-size: 15px; color: var(--ink);
  }
  .contacts li.contacts__email { font-weight: 400; font-size: 14px; }
  .contacts svg { width: 33px; height: 33px; margin-right: 6px; flex: none; }
  .corner-triangle { position: absolute; left: 13px; top: 251px; }
  .website {
    position: absolute; left: 0; width: 600px; top: 290px; text-align: center;
    font-family: "Lora", serif; font-size: 19px; color: var(--ink);
  }
  .website em { font-style: normal; color: var(--gold); }
  .social { position: absolute; left: 511px; top: 286px; display: flex; gap: 2px; }
  .social span { width: 24px; height: 24px; border-radius: 50%; background: #3a3a3a; }
</style>
</head>
<body>
<main class="canvas">

  <section class="card-front" aria-label="Card front">
    <div class="card-front__texture" role="img" aria-label="Dark hexagon mesh texture"></div>
    <div class="card-front__frame"></div>
    <div class="brand-mark">
      <span class="brand-mark__line">KORVAL</span>
      <span class="brand-mark__line brand-mark__line--sub">STUDIO</span>
    </div>
  </section>

  <section class="card-back" aria-label="Card back">
    <div class="card-back__texture" role="img" aria-label="Faint light hexagon pattern"></div>
    <div class="corner-brand">KORVAL<br>STUDIO</div>
    <div class="faint-brand"><span>KORVAL</span><span>STUDIO</span></div>

    <p class="address">ADDRESS ADDRESS ADDRESS</p>
    <div class="divider"></div>

    <div class="person">
      <p class="person__name">Name of Client</p>
      <p class="person__role">Architect</p>
    </div>

    <ul class="contacts">
      <li>
        <svg viewBox="0 0 34 34" aria-hidden="true"><circle cx="17" cy="17" r="15.5" fill="#fff" stroke="#333" stroke-width="2"/><path d="M12 9c1-1 2-1 3 0l2 3c.5 1 .3 1.8-.5 2.4l-1 .8c.8 2 2.4 3.8 4.4 4.8l.9-1c.7-.8 1.6-.9 2.4-.3l2.8 2c1 .8 1 1.8 0 2.8l-1.2 1.2c-1.4 1.4-4 1-7-1.2-3-2.2-5.6-5.4-6.7-8.4-.8-2.4-.6-4.3.4-5.3z" fill="#333"/></svg>
        +44 (0) 207 555 0142
      </li>
      <li>
        <svg viewBox="0 0 34 34" aria-hidden="true"><circle cx="17" cy="17" r="15.5" fill="#fff" stroke="#333" stroke-width="2"/><path d="M12 9c1-1 2-1 3 0l2 3c.5 1 .3 1.8-.5 2.4l-1 .8c.8 2 2.4 3.8 4.4 4.8l.9-1c.7-.8 1.6-.9 2.4-.3l2.8 2c1 .8 1 1.8 0 2.8l-1.2 1.2c-1.4 1.4-4 1-7-1.2-3-2.2-5.6-5.4-6.7-8.4-.8-2.4-.6-4.3.4-5.3z" fill="#333"/></svg>
        +971 555 014 276
      </li>
      <li class="contacts__email">
        <svg viewBox="0 0 34 34" aria-hidden="true"><circle cx="17" cy="17" r="15.5" fill="#fff" stroke="#333" stroke-width="2"/><rect x="8" y="11" width="18" height="12" rx="1" fill="#333"/><path d="M8.5 11.5l8.5 7 8.5-7" fill="none" stroke="#fff" stroke-width="1.4"/></svg>
        email@email.com
      </li>
    </ul>

    <svg class="corner-triangle" width="51" height="59" viewBox="0 0 51 59" aria-hidden="true"><polygon points="0,0 0,59 51,59" fill="#333"/></svg>

    <p class="website">www.<em>korvalstudio</em>.com</p>
    <div class="social" aria-hidden="true"><span></span><span></span></div>
  </section>

</main>
</body>
</html>
```